Until now, Brisk Technology was exclusively geared towards marketing the self-warming toasty-toes insole. Corresponding designer material exists for this purpose, which is further used in this line of business. In the meantime, the business purpose has been expanded to include the following activities: "The company provides consulting services and takes on board mandates in the field of energy and information technology as well as personality-enhancing coaching." We now need a suitable stationery design (letterhead, business card) for this new business purpose. The design is intended to convey specialist knowledge and many years of experience

```html
<!DOCTYPE html>
<html lang="en">
<head>
<meta charset="utf-8">
<title>Brisk Technology – Business Card</title>
<link href="https://fonts.googleapis.com/css2?family=Lato:wght@400;700;900&family=Oswald:wght@500&display=swap" rel="stylesheet">
<style>
  :root {
    --stage: #1b1b1b;
    --card: #111112;
    --brand-blue: #2477c4;
    --text-light: #f2f2f2;
    --rule: #8a8a8a;
  }
  * { margin: 0; padding: 0; box-sizing: border-box; }
  html, body { width: 1200px; height: 900px; overflow: hidden; }
  body {
    background: var(--stage);
    font-family: "Lato", sans-serif;
    position: relative;
  }
  .card {
    position: absolute;
    left: 300px;
    width: 600px;
    height: 340px;
    background: var(--card);
    overflow: hidden;
    box-shadow: 0 10px 24px rgba(0,0,0,.55);
  }
  .card--front { top: 80px; }
  .card--back { top: 480px; }
  .card__band {
    position: absolute;
    left: 0; right: 0; bottom: 0;
    height: 12px;
    background: var(--brand-blue);
  }
  .brand {
    position: absolute;
    top: 130px;
    left: 0; right: 0;
    display: flex;
    align-items: center;
    justify-content: center;
    gap: 16px;
  }
  .brand__square {
    width: 40px; height: 40px;
    background: var(--brand-blue);
  }
  .brand__name {
    font-weight: 700;
    font-size: 42px;
    color: var(--brand-blue);
    letter-spacing: .5px;
  }
  .person {
    position: absolute;
    top: 120px;
    right: 320px;
    text-align: right;
  }
  .person__name {
    font-family: "Oswald", sans-serif;
    font-weight: 500;
    font-size: 36px;
    line-height: 1.05;
    color: var(--brand-blue);
    text-transform: uppercase;
    letter-spacing: -.5px;
  }
  .person__role {
    font-size: 18px;
    color: var(--text-light);
    margin-top: 2px;
  }
  .divider {
    position: absolute;
    left: 298px;
    top: 122px;
    width: 1px;
    height: 96px;
    background: var(--rule);
  }
  .contacts {
    position: absolute;
    left: 320px;
    top: 128px;
    list-style: none;
  }
  .contacts__item {
    display: flex;
    align-items: center;
    gap: 10px;
    font-size: 18px;
    color: var(--text-light);
    line-height: 30px;
  }
  .contacts__icon { width: 18px; height: 18px; flex: none; }
  .address {
    position: absolute;
    left: 0; right: 0;
    top: 262px;
    text-align: center;
    font-size: 19px;
    color: var(--text-light);
  }
</style>
</head>
<body>
  <section class="card card--front">
    <div class="brand">
      <span class="brand__square"></span>
      <span class="brand__name">Brisk Technology</span>
    </div>
    <div class="card__band"></div>
  </section>

  <section class="card card--back">
    <div class="person">
      <p class="person__name">Lukas Brenner</p>
      <p class="person__role">Managing Director</p>
    </div>
    <div class="divider"></div>
    <ul class="contacts">
      <li class="contacts__item">
        <svg class="contacts__icon" viewBox="0 0 24 24" aria-hidden="true"><path fill="var(--brand-blue)" d="M6.6 10.8a15.1 15.1 0 0 0 6.6 6.6l2.2-2.2c.3-.3.7-.4 1-.2 1.1.4 2.3.6 3.6.6.6 0 1 .4 1 1V20c0 .6-.4 1-1 1A17 17 0 0 1 3 4c0-.6.4-1 1-1h3.5c.6 0 1 .4 1 1 0 1.3.2 2.5.6 3.6.1.3 0 .7-.2 1z"/></svg>
        <span>044-987 654 321</span>
      </li>
      <li class="contacts__item">
        <svg class="contacts__icon" viewBox="0 0 24 24" aria-hidden="true"><rect x="2" y="5" width="20" height="14" fill="none" stroke="var(--brand-blue)" stroke-width="2"/><path d="M2 5l10 8 10-8" fill="none" stroke="var(--brand-blue)" stroke-width="2"/></svg>
        <span>info@brisktech.ch</span>
      </li>
      <li class="contacts__item">
        <svg class="contacts__icon" viewBox="0 0 24 24" aria-hidden="true"><g fill="none" stroke="var(--brand-blue)" stroke-width="1.8"><circle cx="12" cy="12" r="9.5"/><ellipse cx="12" cy="12" rx="4.5" ry="9.5"/><path d="M2.5 12h19M4 7h16M4 17h16"/></g></svg>
        <span>www.brisktech.ch</span>
      </li>
    </ul>
    <p class="address">Talweg 14 , CH - 8900 Hofwil</p>
    <div class="card__band"></div>
  </section>
</body>
</html>
```